Powerpoint visual improvements

I need a cover page, and our beliefs page and differentiating factors page / graphic design for our presentation. For the cover page I would just like an attractive design that incorporate our architectural concept with columns and potentially our logo. For the beliefs page I just want a more attractive presentatoin of the concepts. For the differentiating factors page I want a graphic that captures the points about how we are different from competitors. I have used the attached content to date, but I think it can be improved. The text is included in the graphic and I would also like to make sure the firm logo is incorporated.

Target Market(s)

Individual and institutional investors.

Industry/Entity Type

Investment Advisory

Requirements
Must have
• Our corporate colors are generally RGB 145,148,149; 66,68,76; 0,0,153; and 0,63,127. Our logo is attached. Our primary font is Georgia. Our website is www.PelmarCW.com. The key pages are www.PelmarCW.com/beliefs and www.PelmarCW.com/value we are trying to capture in a presentation. We also need a new presentation cover. Use the website as a reference for the type of imagery we like.

```html
<!DOCTYPE html>
<html lang="en">
<head>
<meta charset="utf-8">
<title>Pelmar Asset Management – Beliefs and Difference</title>
<link href="https://fonts.googleapis.com/css2?family=Bebas+Neue&family=EB+Garamond:wght@400&family=Oswald:wght@300&display=swap" rel="stylesheet">
<style>
  :root {
    --navy: #0b2d6b;
    --text-grey: #6f6f6f;
    --label-grey: #7a7a7a;
    --page: #ffffff;
    --canvas: #ffffff;
    --photo-warm: #b8864a;
    --photo-stone: #9a9288;
    --photo-light: #ddd8d0;
  }
  * { margin: 0; padding: 0; box-sizing: border-box; }
  html, body { width: 1000px; height: 1200px; overflow: hidden; background: var(--canvas); }
  body { position: relative; font-family: "EB Garamond", Georgia, serif; }

  .slide {
    position: absolute; left: 27px; width: 947px; height: 532px;
    background: var(--page);
    box-shadow: 2px 3px 5px rgba(0,0,0,0.45);
  }
  .slide--beliefs { top: 19px; }
  .slide--difference { top: 572px; }

  .slide__photo {
    position: absolute; left: 0; top: 0; width: 360px; height: 532px;
    background: linear-gradient(110deg, var(--photo-warm) 0%, var(--photo-stone) 35%, var(--photo-light) 60%, var(--photo-stone) 100%);
  }

  .abs { position: absolute; }
  .center { transform: translateX(-50%); text-align: center; }

  .heading {
    font-family: "Bebas Neue", Impact, sans-serif; color: var(--navy); font-weight: 400;
  }
  .beliefs__title { left: 652px; top: 24px; font-size: 37px; line-height: 1; }
  .beliefs__intro {
    left: 652px; top: 73px; width: 535px; font-size: 13.6px; line-height: 19px; color: var(--text-grey); letter-spacing: 0.1px;
  }

  .belief { width: 130px; }
  .belief__name {
    font-family: "Oswald", "Arial Narrow", sans-serif; font-weight: 300; color: var(--navy);
    font-size: 21px; line-height: 24px; text-transform: uppercase; letter-spacing: -0.4px; white-space: nowrap;
  }
  .belief__text { width: 118px; margin: 4px auto 0; font-size: 9.3px; line-height: 12.4px; color: var(--text-grey); }
  .belief--cost { left: 498px; top: 200px; }
  .belief--research { left: 764px; top: 200px; }
  .belief--focus { left: 498px; top: 355px; }
  .belief--access { left: 764px; top: 355px; }

  .diagram { position: absolute; left: 0; top: 0; width: 947px; height: 532px; pointer-events: none; }

  .brand-mark {
    position: absolute; border-radius: 50%; background: var(--navy); width: 74px; height: 74px;
    display: flex; align-items: center; justify-content: center;
    font-family: "Bebas Neue", Impact, sans-serif; color: #fff; font-size: 19px; letter-spacing: 0.5px;
  }
  .slide--beliefs .brand-mark { left: 597px; top: 264px; }
  .slide--difference .brand-mark { left: 435px; top: 303px; }

  .footer { font-size: 11px; color: var(--label-grey); letter-spacing: 0.3px; }
  .footer__page { font-size: 11px; color: #999; }
  .slide--beliefs .footer { left: 383px; top: 506px; }
  .slide--beliefs .footer__page { left: 890px; top: 506px; }
  .slide--difference .footer { left: 44px; top: 503px; }
  .slide--difference .footer__page { left: 892px; top: 505px; font-size: 8px; }

  .difference__title {
    right: 664px; top: 40px; text-align: right; font-size: 54px; line-height: 62px;
  }
  .difference__copy { left: 287px; top: 38px; width: 520px; color: var(--text-grey); font-size: 13.3px; line-height: 16.6px; }
  .difference__copy p + p { margin-top: 11px; }

  .factor { font-size: 14.5px; line-height: 18.5px; color: var(--label-grey); letter-spacing: 0.5px; text-transform: uppercase; }
  .factor--transparent { left: 351px; top: 232px; }
  .factor--experienced { left: 593px; top: 232px; }
  .factor--institutional { right: 700px; top: 306px; text-align: right; }
  .factor--independent { left: 698px; top: 306px; }
  .factor--proactive { left: 351px; top: 402px; }
  .factor--sound { left: 595px; top: 402px; }
</style>
</head>
<body>

<section class="slide slide--beliefs">
  <div class="slide__photo" role="img" aria-label="Photograph of tall classical stone columns on a building facade in warm sunlight"></div>

  <h1 class="abs center heading beliefs__title">Our Beliefs</h1>
  <p class="abs center beliefs__intro">Lorem Ipsum has been the industry's standard dummy text ever since the 1500s, when an unknown printer took a galley of type and scrambled it to make a type specimen.</p>

  <svg class="diagram" viewBox="0 0 947 532" fill="none" stroke="#0b2d6b" stroke-width="2.2">
    <path d="M496 277 H514 M505 277 V302 H579 M496 339 H514 M505 339 V313 H579"/>
    <path d="M780 277 H762 M771 277 V302 H698 M780 339 H762 M771 339 V313 H698"/>
    <!-- piggy bank icon -->
    <g stroke-width="1.4" stroke-linejoin="round">
      <path d="M482 178 q0 -9 12 -9 h5 q9 0 12 7 l3 0 v6 l-3 1 q-2 4 -5 5 v4 h-4 v-3 h-8 v3 h-4 v-4 q-7 -3 -8 -10z"/>
      <circle cx="497" cy="162" r="3.2"/>
      <circle cx="506" cy="175" r="0.7" fill="#0b2d6b"/>
    </g>
    <!-- magnifier with tick -->
    <g stroke-width="1.7" stroke-linecap="round">
      <circle cx="760" cy="172" r="10"/>
      <circle cx="760" cy="172" r="6.8" stroke-width="1.2"/>
      <path d="M756.5 172 l2.7 2.7 l4.5 -5.5"/>
      <path d="M767 179 l8 8"/>
    </g>
    <!-- target with arrows -->
    <g stroke-width="1.6" stroke-linecap="round">
      <circle cx="497" cy="458" r="12"/>
      <circle cx="497" cy="458" r="7.5"/>
      <circle cx="497" cy="458" r="3"/>
      <path d="M489 430 v10 M486 437 l3 3 l3 -3 M497 430 v10 M494 437 l3 3 l3 -3 M505 430 v10 M502 437 l3 3 l3 -3"/>
    </g>
    <!-- hand pointer -->
    <g stroke-width="1.5" stroke-linecap="round" stroke-linejoin="round">
      <path d="M763 440 v-8 M755 443 l-5 -5 M771 443 l5 -5 M752 450 h-7 M774 450 h7"/>
      <path d="M761 467 v-18 q2 -3 4 0 v12 v-4 q2 -3 4 0 v4 v-3 q2 -3 4 0 v4 v-2 q2 -3 4 0 v9 q0 8 -7 10 h-5 q-4 -1 -7 -6 l-4 -7 q1 -3 4 -1 z"/>
    </g>
  </svg>

  <div class="brand-mark" aria-label="Pelmar">Pelmar</div>

  <div class="abs center belief belief--cost">
    <h2 class="belief__name">Cost Matters</h2>
    <p class="belief__text">Aenean commodo ligula eget dolor. Aenean massa. Cum sociis natoque penatibus.</p>
  </div>
  <div class="abs center belief belief--research">
    <h2 class="belief__name">Research Matters</h2>
    <p class="belief__text">Aenean commodo ligula eget dolor. Aenean massa. Cum sociis natoque penatibus.</p>
  </div>
  <div class="abs center belief belief--focus">
    <h2 class="belief__name">Focus Matters</h2>
    <p class="belief__text">Aenean commodo ligula eget dolor. Aenean massa. Cum sociis natoque penatibus.</p>
  </div>
  <div class="abs center belief belief--access">
    <h2 class="belief__name">Access Matters</h2>
    <p class="belief__text">Aenean commodo ligula eget dolor. Aenean massa. Cum sociis natoque penatibus.</p>
  </div>

  <p class="abs footer">PELMAR &nbsp;|&nbsp; ASSET MANAGEMENT</p>
  <p class="abs footer__page">5</p>
</section>

<section class="slide slide--difference">
  <h1 class="abs heading difference__title">The Pelmar<br>Difference</h1>
  <div class="abs difference__copy">
    <p>Lorem ipsum dolor sit amet, consectetuer adipiscing elit. Aenean commodo ligula eget dolor. Aenean massa. Cum sociis natoque penatibus et magnis dis parturient montes, nascetur ridiculus mus. Donec quam felis, ultricies nec, pellentesque eu, pretium quis, sem. Nulla consequat massa quis enim. Donec pede justo, fringilla vel, aliquet nec, vulputate eget, arcu.</p>
    <p>In enim justo, rhoncus ut, imperdiet a, venenatis vitae, justo. Nullam dictum felis eu pede mollis pretium. Integer tincidunt. Cras dapibus. Vivamus elementum semper nisi. Aenean vulputate eleifend tellus. Aenean leo ligula, porttitor eu, consequat vitae, eleifend ac, enim.</p>
  </div>

  <svg class="diagram" viewBox="0 0 947 532" fill="none" stroke="#0b2d6b" stroke-width="2.2">
    <path d="M342 294 H361 M351 294 V319 H425"/>
    <path d="M268 331 V349 M268 340 H425"/>
    <path d="M342 384 H361 M351 384 V359 H425"/>
    <path d="M604 294 H586 M595 294 V319 H521"/>
    <path d="M679 331 V349 M679 340 H521"/>
    <path d="M604 384 H586 M595 384 V359 H521"/>
  </svg>

  <div class="brand-mark" aria-label="Pelmar">Pelmar</div>

  <p class="abs center factor factor--transparent">Transparent<br>Communication</p>
  <p class="abs center factor factor--experienced">Experienced<br>Investors</p>
  <p class="abs factor factor--institutional">Institutional<br>Research<br>Process</p>
  <p class="abs factor factor--independent">Independent<br>Portfolio<br>Construction</p>
  <p class="abs center factor factor--proactive">Proactive Total<br>Fee<br>Management</p>
  <p class="abs center factor factor--sound">Sound<br>Operational<br>Platform</p>

  <p class="abs footer">PELMAR &nbsp;|&nbsp; ASSET MANAGEMENT</p>
  <p class="abs footer__page">6</p>
</section>

</body>
</html>
```